iPhone iOS 7 App For Managing Tasks/Photos for Internal Company Use

We need an app design that displays company objectives and task, and provides the interface for employees to complete a task by uploading a photo and adding comments.

Please see attached mock up sketches as a rough guideline

Final delivery of files must contain PSD, and all layers/objects sliced both is PSD and PNG files

Target Market(s)

This is a tool for internal employee use

Industry/Entity Type

It Company

Requirements
Must have
• Must include logo, and match the colour scheme
Use iPhone iOS 7 Style

```html
<!DOCTYPE html>
<html lang="en">
<head>
<meta charset="utf-8">
<title>Objectives – Task Manager</title>
<link rel="stylesheet" href="https://fonts.googleapis.com/css2?family=Carlito:wght@400;700&family=Arimo:wght@400;700&display=swap">
<style>
  :root {
    --bg: #a8bbc6;
    --white: #ffffff;
    --brand: #4f7880;
    --ink: #3f4a4f;
    --ink-dark: #111111;
    --task-ink: #8a9196;
    --panel-top: #eef2f4;
    --panel-bottom: #c9d5dc;
    --panel-edge: #8a9aa3;
    --active-top: #7b939b;
    --active-mid: #5f7880;
    --task-bg: #dfe6ea;
    --rule: #7d8f96;
    --tick: #e8452c;
    --nav: #587880;
    --nav-dark: #48656c;
    --nav-disc: #e6eaec;
    --nav-icon: #6f8890;
  }
  * { box-sizing: border-box; margin: 0; padding: 0; }
  html, body { width: 675px; height: 1200px; overflow: hidden; }
  body { background: var(--bg); font-family: "Carlito", "Calibri", sans-serif; position: relative; }

  .status-bar {
    position: absolute; top: 0; left: 0; width: 675px; height: 50px;
    font-family: "Arimo", Arial, sans-serif; font-size: 22px; color: var(--ink-dark);
  }
  .status-bar .carrier { position: absolute; left: 12px; top: 11px; display: flex; align-items: center; gap: 4px; }
  .status-bar .time { position: absolute; left: 0; right: 0; top: 11px; text-align: center; font-weight: 700; }
  .status-bar .battery { position: absolute; right: 12px; top: 11px; display: flex; align-items: center; gap: 8px; }

  .app-header {
    position: absolute; top: 51px; left: 0; width: 675px; height: 84px; background: var(--white);
    box-shadow: 0 2px 4px rgba(0,0,0,.25);
    display: flex; align-items: center; justify-content: center; gap: 12px;
  }
  .brand-dot { width: 40px; height: 40px; border-radius: 50%; background: var(--brand); }
  .brand-name { font-size: 36px; font-weight: 700; color: var(--brand); letter-spacing: .5px; }

  .panel {
    position: absolute; left: 137px; width: 440px;
    background: linear-gradient(var(--panel-top), var(--panel-bottom));
    border: 1px solid var(--panel-edge); border-radius: 4px;
    box-shadow: 0 1px 3px rgba(0,0,0,.25);
  }
  .objective-picker { top: 281px; height: 82px; display: flex; align-items: center; padding-left: 28px; }
  .objective-picker .label { font-size: 29px; font-weight: 700; color: var(--ink); margin-left: 12px; }
  .objective-picker .chevron { position: absolute; right: 24px; top: 33px; }
  .picker-pointer { position: absolute; left: 530px; top: 380px; }

  .objective {
    position: absolute; left: 137px; width: 440px; height: 80px;
    display: flex; align-items: center; padding-left: 85px;
    font-size: 29px; font-weight: 700; color: var(--ink);
    background: linear-gradient(var(--panel-top), var(--panel-bottom));
    border: 1px solid var(--panel-edge);
  }
  .objective.first { top: 394px; border-radius: 4px 4px 0 0; }
  .objective.active {
    top: 474px; color: #2f3a3e;
    background: linear-gradient(var(--active-top), var(--active-mid) 50%, var(--active-top));
    border-radius: 0 0 4px 4px;
  }
  .objective.third { top: 838px; border-radius: 4px 4px 0 0; border-bottom: 2px solid #5d6b70; }
  .objective.fourth { top: 918px; border-radius: 0 0 4px 4px; border-top: none; }

  .task-list {
    position: absolute; left: 142px; top: 561px; width: 430px; height: 273px;
    background: var(--task-bg); border: 1px solid #b9c6cc;
    font-family: "Arimo", Arial, sans-serif;
  }
  .task {
    position: absolute; left: 24px; width: 377px; height: 68px;
    display: flex; align-items: center; padding-left: 25px;
    font-size: 20px; font-weight: 700; color: var(--task-ink);
    border-bottom: 2px solid var(--rule);
  }
  .task:last-of-type { border-bottom: none; }
  .task .tick { position: absolute; right: 16px; top: 16px; }
  .scroll-track {
    position: absolute; left: 410px; top: 11px; width: 12px; height: 257px;
    border: 1px solid #a9b3b8; border-radius: 6px; background: #eef2f4;
  }
  .scroll-thumb { position: absolute; left: 1px; top: 62px; width: 8px; height: 82px; border-radius: 4px; background: #9aa4a8; }

  .tab-bar { position: absolute; left: 0; top: 1040px; width: 675px; height: 160px; }
  .tab-track { position: absolute; left: 0; top: 0; }
  .tab {
    position: absolute; width: 140px; text-align: center; top: 98px;
    font-size: 29px; font-weight: 700; color: var(--brand);
  }
</style>
</head>
<body>

<div class="status-bar">
  <div class="carrier">
    <svg width="74" height="14" viewBox="0 0 74 14" aria-hidden="true">
      <circle cx="7" cy="7" r="6" fill="#111"/><circle cx="21" cy="7" r="6" fill="#111"/><circle cx="35" cy="7" r="6" fill="#111"/>
      <circle cx="49" cy="7" r="5.5" fill="none" stroke="#111"/><circle cx="63" cy="7" r="5.5" fill="none" stroke="#111"/>
    </svg>
    <span>NOVA</span>
    <svg width="26" height="20" viewBox="0 0 26 20" aria-hidden="true">
      <path d="M13 18 L9 14 A6 6 0 0 1 17 14 Z" fill="#111"/>
      <path d="M5 10 A12 12 0 0 1 21 10" fill="none" stroke="#111" stroke-width="3"/>
      <path d="M1 6 A17 17 0 0 1 25 6" fill="none" stroke="#111" stroke-width="3"/>
    </svg>
  </div>
  <div class="time">4:21 PM</div>
  <div class="battery">
    <svg width="14" height="22" viewBox="0 0 14 22" aria-hidden="true">
      <path d="M2 6 L12 16 L7 21 V1 L12 6 L2 16" fill="none" stroke="#111" stroke-width="2"/>
    </svg>
    <span>100%</span>
    <svg width="52" height="22" viewBox="0 0 52 22" aria-hidden="true">
      <rect x="1" y="1" width="46" height="20" rx="4" fill="none" stroke="#111" stroke-width="2"/>
      <rect x="4" y="4" width="40" height="14" rx="2" fill="#111"/>
      <rect x="48" y="7" width="3" height="8" rx="1" fill="#111"/>
    </svg>
  </div>
</div>

<header class="app-header">
  <span class="brand-dot"></span>
  <span class="brand-name">ORBITRA COMPANY NAME</span>
</header>

<div class="panel objective-picker">
  <svg width="36" height="30" viewBox="0 0 36 30" aria-hidden="true">
    <circle cx="14" cy="15" r="12" fill="none" stroke="#4a5357" stroke-width="3"/>
    <circle cx="14" cy="15" r="6" fill="none" stroke="#4a5357" stroke-width="3"/>
    <line x1="14" y1="15" x2="34" y2="10" stroke="#4a5357" stroke-width="3"/>
    <path d="M28 6 L35 9 L30 14" fill="#4a5357"/>
  </svg>
  <span class="label">Select An Objective</span>
  <svg class="chevron" width="22" height="14" viewBox="0 0 22 14" aria-hidden="true">
    <path d="M2 2 L11 11 L20 2" fill="none" stroke="#4a5357" stroke-width="4"/>
  </svg>
</div>
<svg class="picker-pointer" width="24" height="15" viewBox="0 0 24 15" aria-hidden="true">
  <path d="M0 15 L12 2 L24 15" fill="#eef2f4" stroke="#8a9aa3"/>
</svg>

<div class="objective first">Objective 1</div>
<div class="objective active">Objective 2</div>

<div class="task-list">
  <div class="task" style="top:2px">Task 1
    <svg class="tick" width="36" height="32" viewBox="0 0 36 32" aria-hidden="true"><path d="M3 17 L13 27 L33 4" fill="none" stroke="var(--tick)" stroke-width="5"/></svg>
  </div>
  <div class="task" style="top:70px">Task 2
    <svg class="tick" width="36" height="32" viewBox="0 0 36 32" aria-hidden="true"><path d="M3 17 L13 27 L33 4" fill="none" stroke="var(--tick)" stroke-width="5"/></svg>
  </div>
  <div class="task" style="top:138px">Task 3
    <svg class="tick" width="36" height="32" viewBox="0 0 36 32" aria-hidden="true"><path d="M3 17 L13 27 L33 4" fill="none" stroke="var(--tick)" stroke-width="5"/></svg>
  </div>
  <div class="task" style="top:206px">Task 4</div>
  <div class="scroll-track"><div class="scroll-thumb"></div></div>
</div>

<div class="objective third">Objective 3</div>
<div class="objective fourth">Objective 4</div>

<nav class="tab-bar">
  <svg class="tab-track" width="675" height="100" viewBox="0 0 675 100" aria-hidden="true">
    <path d="M103 40 C180 30 190 55 264 40 C340 30 350 55 422 40 C500 30 510 55 583 40" fill="none" stroke="var(--nav)" stroke-width="18"/>
    <g fill="var(--nav)">
      <circle cx="103" cy="49" r="42"/><circle cx="264" cy="49" r="42"/>
      <circle cx="422" cy="49" r="42"/><circle cx="583" cy="49" r="42"/>
    </g>
    <g fill="var(--nav-disc)" stroke="var(--nav-dark)" stroke-width="2">
      <circle cx="103" cy="49" r="32"/><circle cx="264" cy="49" r="32"/>
      <circle cx="422" cy="49" r="32"/><circle cx="583" cy="49" r="32"/>
    </g>
    <g fill="var(--nav-icon)">
      <path d="M82 50 L103 31 L124 50 H118 V68 H108 V56 H98 V68 H88 V50 Z"/>
      <path d="M408 54 L428 34 L436 62 Z"/><rect x="403" y="52" width="9" height="10" transform="rotate(-40 407 57)"/>
      <path d="M570 30 H592 V36 H586 V66 L570 70 Z"/>
      <path d="M588 46 H596 V40 L606 50 L596 60 V54 H588 Z"/>
    </g>
    <g fill="none" stroke="var(--nav-icon)" stroke-width="4">
      <circle cx="260" cy="52" r="16"/><circle cx="260" cy="52" r="8"/>
      <path d="M260 52 L282 40"/>
      <path d="M438 38 A16 16 0 0 1 442 56" stroke-width="3"/>
    </g>
  </svg>
  <span class="tab" style="left:33px">Home</span>
  <span class="tab" style="left:194px">Objectives</span>
  <span class="tab" style="left:347px">News</span>
  <span class="tab" style="left:511px">Log Out</span>
</nav>

</body>
</html>
```